Business Card Design Project

i have the logo designed.
I require designs for the managing director and the general manager.
we need space for email, and a mobile number.
any other cool stuff/design you guys just let me see what you got.
The managing director card could be black, minimalist, and the cards for the rest of the company could be using the green logo.
it has to impress. transportation market is fragmented, we want to appear professional and sophisticated.
Md: Tarek bani rahim
General manager: omer rahim
clients: procurement heads of contracting companies
Business

```html
<!DOCTYPE html>
<html lang="en">
<head>
<meta charset="utf-8">
<title>Velora – Managing Director Business Card</title>
<link href="https://fonts.googleapis.com/css2?family=Oswald:wght@400;600&display=swap" rel="stylesheet">
<style>
  :root {
    --backdrop: #c9c9c9;
    --card-black: #0b0b0b;
    --card-shade: #1a1a1a;
    --ink-white: #ffffff;
    --ink-black: #0b0b0b;
  }
  * { margin: 0; padding: 0; box-sizing: border-box; }
  html, body {
    width: 1200px; height: 1000px; overflow: hidden;
    background: var(--backdrop);
    font-family: "Oswald", "Arial Narrow", sans-serif;
  }
  .canvas { position: relative; width: 1200px; height: 1000px; }

  .card {
    position: absolute;
    width: 630px; height: 360px;
    background: var(--card-black);
    overflow: hidden;
  }
  .card--front { left: 430px; top: 110px; }
  .card--back  { left: 140px; top: 530px; }

  .front-swoosh, .back-swoosh { position: absolute; inset: 0; }

  .brand {
    position: absolute; left: 0; right: 0; top: 140px;
    display: flex; align-items: center; justify-content: center; gap: 18px;
  }
  .brand__dot {
    width: 26px; height: 26px; border-radius: 50%;
    background: var(--ink-white);
  }
  .brand__name {
    color: var(--ink-white);
    font-weight: 600; font-size: 64px; letter-spacing: 2px;
    line-height: 1; text-transform: uppercase;
  }

  .back-decoration {
    position: absolute; left: 40px; top: 20px; width: 330px; height: 190px;
    background: radial-gradient(ellipse at 40% 50%, #181818 0%, rgba(11,11,11,0) 70%);
  }
  .divider {
    position: absolute; left: 44px; top: 222px;
    width: 560px; height: 4px; background: var(--ink-white);
  }
  .contact {
    position: absolute; left: 44px; top: 236px;
    list-style: none; color: var(--ink-white);
    font-size: 15px; line-height: 22px; text-transform: uppercase;
  }
  .person {
    position: absolute; right: 30px; top: 168px; text-align: right;
  }
  .person__name {
    color: var(--ink-white); font-weight: 600;
    font-size: 40px; line-height: 46px; text-transform: uppercase;
    letter-spacing: 1px;
  }
  .person__title {
    display: inline-block; margin-top: 14px;
    background: var(--ink-white); color: var(--ink-black);
    font-weight: 600; font-size: 20px; line-height: 26px;
    padding: 0 10px; text-transform: uppercase;
  }
</style>
</head>
<body>
<main class="canvas">

  <section class="card card--front" aria-label="Card front">
    <svg class="front-swoosh" viewBox="0 0 630 360" aria-hidden="true">
      <path d="M0 90 C160 40 360 60 630 20 L630 70 C420 110 200 90 0 140 Z" fill="#151515"/>
      <path d="M120 330 C300 250 480 270 630 200 L630 260 C470 320 320 310 160 360 L100 360 Z" fill="#141414"/>
    </svg>
    <div class="brand">
      <span class="brand__dot"></span>
      <span class="brand__name">Velora</span>
    </div>
  </section>

  <section class="card card--back" aria-label="Card back">
    <div class="back-decoration" role="img" aria-label="Faint brand decoration in dark grey"></div>
    <div class="divider"></div>
    <ul class="contact">
      <li>managingdirector@velora.com</li>
      <li>+65 4170 5290</li>
      <li>www.velora.com</li>
    </ul>
    <div class="person">
      <div class="person__name">Tarek Bani Rahim</div>
      <div class="person__title">Managing Director</div>
    </div>
  </section>

</main>
</body>
</html>
```